Quillmore Website design

Create a sophisticated minimalist shopify ecommerce store that can be integrated with stockwise hub POS.

Quillmore is a Brick and mortar store that is focused on exceptional customer service and quality Ladies fashion and specialty swimwear for Women, Men and Children.

This website will need to be easy to navigate by the end user and manage inhouse.

With so many different product categories and customer demographics it will be difficult to make seamless and easy to navigate.

Think The Varnel, Lumo etc where there are Women, Men and Kids

It would be fantastic to build a site with three different navigations to constant themes that are modified to suit each demographic.

We have a logo to use and would like the theme to be easily updated as seasons change and our business evolves.

The website must be set up to use SEO for google and other leading search engines.

Stock will be supplied from either our brick and mortar store or warehouse so would need to consist of multiple store locations as far as the back end is concerned.

It will need to be set up with apps that allow us to stream line our fullfilment in house (label printing, picking lists and shipping with Kestrel Freight)

```html
<!DOCTYPE html>
<html lang="en">
<head>
<meta charset="utf-8">
<title>Quillmore — Ladies Fashion &amp; Swimwear</title>
<link rel="stylesheet" href="https://fonts.googleapis.com/css2?family=Big+Shoulders+Display:wght@200;300&family=Poppins:wght@400;500;600&display=swap">
<style>
  :root {
    --sage: #76866a;
    --sage-dark: #66765b;
    --ink: #2b2b2b;
    --muted: #555;
    --paper: #ffffff;
    --band: #f3f3f0;
    --line: #c9cfc3;
  }
  * { margin: 0; padding: 0; box-sizing: border-box; }
  html, body { width: 1200px; height: 4240px; overflow: hidden; background: var(--paper); }
  body { position: relative; font-family: "Poppins", sans-serif; color: var(--ink); }
  .abs { position: absolute; }
  .display { font-family: "Big Shoulders Display", sans-serif; font-weight: 200; text-transform: uppercase; letter-spacing: 1px; }
  .photo-fill { box-shadow: inset 0 0 120px rgba(0,0,0,.18); }

  /* header */
  .site-header { left: 0; top: 0; width: 1200px; height: 132px; background: var(--paper); }
  .brand-box { left: 81px; top: 0; width: 240px; height: 189px; background: var(--sage); outline: 2px solid #fff; outline-offset: -6px; z-index: 3; display: flex; align-items: flex-end; justify-content: center; padding-bottom: 22px; }
  .brand-box span { color: #fff; font-size: 46px; line-height: 1; }
  .main-nav { top: 88px; left: 418px; }
  .main-nav a { position: absolute; white-space: nowrap; font-size: 14px; letter-spacing: 1px; color: var(--ink); text-decoration: none; }
  .header-icons { top: 26px; left: 975px; display: flex; gap: 22px; }
  .header-icons svg { width: 32px; height: 32px; stroke: var(--ink); fill: none; stroke-width: 1.8; }
  .cart-count { position: absolute; left: 122px; top: -4px; width: 16px; height: 16px; border-radius: 50%; background: var(--sage); color: #fff; font-size: 9px; text-align: center; line-height: 16px; }

  /* hero */
  .hero { left: 0; top: 132px; width: 1200px; height: 589px;
    background:
      radial-gradient(ellipse 180px 300px at 430px 330px, rgba(233,183,64,.85), transparent 70%),
      radial-gradient(ellipse 170px 300px at 620px 360px, rgba(226,170,170,.85), transparent 70%),
      radial-gradient(ellipse 260px 200px at 520px 150px, rgba(150,100,70,.8), transparent 70%),
      linear-gradient(100deg, #2f4a2b 0%, #4f6a3e 25%, #3c5534 55%, #2a3f27 75%, #1f3420 100%); }
  .hero-copy { right: 128px; top: 350px; text-align: right; color: #fff; }
  .hero-copy h1 { font-size: 72px; line-height: 1; font-weight: 200; }
  .hero-copy p { font-size: 27px; line-height: 30px; margin-top: 14px; }
  .btn-shop { display: inline-block; margin-top: 24px; width: 146px; height: 48px; border-radius: 24px; background: var(--sage); color: #fff; font-size: 24px; line-height: 48px; text-align: center; }

  .section-title { width: 1200px; left: 0; text-align: center; color: var(--sage); font-size: 64px; line-height: 1; }

  /* collections */
  .collection { top: 925px; height: 365px; }
  .collection .label { position: absolute; left: 26px; bottom: 22px; color: #fff; font-size: 44px; line-height: 1; }
  .collection svg { position: absolute; right: 20px; bottom: 32px; width: 32px; height: 16px; stroke: #fff; stroke-width: 2; fill: none; }

  /* products */
  .product { width: 226px; text-align: center; }
  .product .photo { width: 226px; height: 305px; position: relative; }
  .product .shop-now { position: absolute; left: 0; bottom: 0; width: 100%; height: 46px; background: rgba(118,134,106,.85); color: #fff; font-size: 22px; line-height: 46px; letter-spacing: 3px; }
  .product .name { margin-top: 18px; font-size: 13.5px; line-height: 17px; color: var(--muted); }
  .product .price { margin-top: 12px; font-size: 16px; font-weight: 600; }

  .band { left: 0; top: 2033px; width: 1200px; height: 708px; background: var(--band); }

  /* about */
  .about-photo { left: 28px; top: 2858px; width: 321px; height: 357px;
    background:
      radial-gradient(ellipse 90px 150px at 170px 200px, rgba(245,243,238,.95), transparent 75%),
      radial-gradient(ellipse 110px 40px at 170px 70px, rgba(240,238,232,.9), transparent 75%),
      linear-gradient(160deg, #24402a, #3e6136 50%, #2b4a2c); }
  .about-title { left: 400px; width: 420px; top: 2950px; text-align: center; color: var(--sage); font-size: 62px; line-height: 1; }
  .about-text { left: 400px; width: 420px; top: 3036px; text-align: center; font-size: 15px; line-height: 25px; color: var(--muted); }

  /* banners */
  .banner { top: 3383px; height: 383px; }
  .banner h2 { position: absolute; top: 58px; color: #fff; font-size: 46px; line-height: 58px; font-weight: 200; }

  /* footer */
  .site-footer { left: 0; top: 3832px; width: 1200px; height: 408px; background: var(--sage); color: #fff; }
  .footer-brand { position: absolute; left: 127px; top: 186px; font-size: 46px; line-height: 1; }
  .footer-col { position: absolute; top: 92px; }
  .footer-col h3 { font-size: 40px; font-weight: 200; line-height: 40px; margin-bottom: 16px; }
  .footer-col a { display: block; color: #fff; text-decoration: none; font-size: 15px; line-height: 29.5px; }
  .footer-rule { position: absolute; left: 127px; right: 127px; top: 295px; border-top: 1px solid rgba(255,255,255,.35); }
  .social { position: absolute; top: 339px; width: 36px; height: 36px; border: 2px solid #fff; border-radius: 50%; display: flex; align-items: center; justify-content: center; }
  .social svg { width: 16px; height: 16px; stroke: #fff; fill: none; stroke-width: 2; }
  .legal { position: absolute; top: 348px; font-size: 15px; }
</style>
</head>
<body>

<header class="abs site-header">
  <div class="abs brand-box"><span class="display">Quillmore</span></div>
  <nav class="abs main-nav">
    <a style="left:0">HOME</a>
    <a style="left:91px">LADIES FASHION</a>
    <a style="left:263px">SWIMWEAR</a>
    <a style="left:397px">ABOUT</a>
    <a style="left:496px">REVIEWS</a>
    <a style="left:607px">CONTACT</a>
  </nav>
  <div class="abs header-icons">
    <svg viewBox="0 0 24 24" aria-label="Wishlist"><path d="M12 20s-7-4.5-8.5-9A4.5 4.5 0 0 1 12 7a4.5 4.5 0 0 1 8.5 4C19 15.5 12 20 12 20z"/></svg>
    <svg viewBox="0 0 24 24" aria-label="Account"><circle cx="12" cy="8" r="4"/><path d="M4 21c0-4 3.5-6.5 8-6.5s8 2.5 8 6.5z"/></svg>
    <svg viewBox="0 0 24 24" aria-label="Cart"><path d="M5 8h14l-1 13H6z"/><path d="M9 8V6a3 3 0 0 1 6 0v2"/></svg>
    <span class="cart-count">0</span>
  </div>
</header>

<section class="abs hero photo-fill" role="img" aria-label="Two smiling women in yellow and pink swimsuits among tropical leaves"></section>
<div class="abs hero-copy">
  <h1 class="display">Quillmore</h1>
  <p>Quillmore is a Brick<br>and mortar store</p>
  <span class="btn-shop display">Shop now</span>
</div>

<h2 class="abs section-title display" style="top:818px">Collection list</h2>
<a class="abs collection photo-fill" style="left:0;width:390px;background:radial-gradient(ellipse 160px 120px at 200px 200px,rgba(222,178,150,.7),transparent 70%),linear-gradient(180deg,#4b95da 0%,#8cbfe8 50%,#a9b8bd 62%,#c6b394 100%)" role="img" aria-label="Three women in bikinis on a beach">
  <span class="label display">Women</span><svg viewBox="0 0 32 16"><path d="M0 8h30M23 1l7 7-7 7"/></svg>
</a>
<a class="abs collection photo-fill" style="left:405px;width:390px;background:radial-gradient(ellipse 70px 150px at 195px 180px,rgba(250,250,250,.85),transparent 70%),linear-gradient(180deg,#eef2f2 0%,#c6dede 45%,#a8cccd 60%,#d6cdbb 100%)" role="img" aria-label="Man in white tee and tropical swim shorts on a beach">
  <span class="label display">Men</span><svg viewBox="0 0 32 16"><path d="M0 8h30M23 1l7 7-7 7"/></svg>
</a>
<a class="abs collection photo-fill" style="left:808px;width:392px;background:radial-gradient(ellipse 150px 130px at 200px 200px,rgba(120,80,60,.55),transparent 70%),linear-gradient(180deg,#c9cbc6 0%,#a6b1ae 45%,#8e9b98 60%,#b5a48a 100%)" role="img" aria-label="Two children running through the surf">
  <span class="label display">Children</span><svg viewBox="0 0 32 16"><path d="M0 8h30M23 1l7 7-7 7"/></svg>
</a>

<h2 class="abs section-title display" style="top:1428px">Our featured</h2>
<div class="abs product" style="left:104px;top:1532px"><div class="photo photo-fill" role="img" aria-label="Woman in white bikini and yellow kaftan by a rocky cove" style="background:radial-gradient(ellipse 70px 110px at 110px 170px,rgba(214,170,40,.8),transparent 70%),linear-gradient(180deg,#7d7f73,#a7a08c 50%,#dcc9a4)"></div><p class="name">Lorem ipsum dolor sit ame<br>nsecteturaelit seius.</p><p class="price">$299.00</p></div>
<div class="abs product" style="left:359px;top:1532px"><div class="photo photo-fill" role="img" aria-label="Woman in striped one-piece on a beach" style="background:radial-gradient(ellipse 60px 90px at 110px 170px,rgba(80,100,180,.7),transparent 70%),radial-gradient(ellipse 60px 40px at 100px 60px,rgba(200,100,60,.6),transparent 70%),linear-gradient(180deg,#d3dfe8,#a9c0d2 55%,#d8cdbb)"></div><p class="name">Lorem ipsum dolor sit ame<br>nsecteturaelit seius.</p><p class="price">$299.00</p></div>
<div class="abs product" style="left:614px;top:1532px"><div class="photo photo-fill" role="img" aria-label="Woman in black one-piece and sun hat on the sand" style="background:radial-gradient(ellipse 50px 90px at 120px 170px,rgba(40,45,40,.75),transparent 70%),linear-gradient(180deg,#e3e6e6,#cbd1d0 50%,#d6cab8)"><span class="shop-now display">Shop now</span></div><p class="name">Lorem ipsum dolor sit ame<br>nsecteturaelit seius.</p><p class="price">$299.00</p></div>
<div class="abs product" style="left:869px;top:1532px"><div class="photo photo-fill" role="img" aria-label="Man in red swim shorts running from the sea" style="background:radial-gradient(ellipse 60px 40px at 110px 200px,rgba(200,50,40,.8),transparent 70%),radial-gradient(ellipse 70px 80px at 110px 110px,rgba(210,160,130,.7),transparent 70%),linear-gradient(180deg,#84aad0,#4f83b6 55%,#c7d8e6)"></div><p class="name">Lorem ipsum dolor sit ame<br>nsecteturaelit seius.</p><p class="price">$299.00</p></div>

<div class="abs band"></div>
<h2 class="abs section-title display" style="top:2140px">Shop our ladies fashion</h2>
<div class="abs product" style="left:104px;top:2244px"><div class="photo photo-fill" role="img" aria-label="Woman in white bikini and cover-up by the sea" style="background:radial-gradient(ellipse 60px 110px at 115px 180px,rgba(248,246,240,.9),transparent 70%),linear-gradient(180deg,#bccdda,#86a3bb 55%,#d6cbb8)"></div><p class="name">Lorem ipsum dolor sit ame<br>nsecteturaelit seius.</p><p class="price">$299.00</p></div>
<div class="abs product" style="left:359px;top:2244px"><div class="photo photo-fill" role="img" aria-label="Woman in red bikini beside a palm trunk" style="background:radial-gradient(ellipse 50px 120px at 90px 170px,rgba(160,100,70,.75),transparent 70%),linear-gradient(180deg,#6f9fc9,#3f74a6 55%,#b9a78a)"></div><p class="name">Lorem ipsum dolor sit ame<br>nsecteturaelit seius.</p><p class="price">$299.00</p></div>
<div class="abs product" style="left:614px;top:2244px"><div class="photo photo-fill" role="img" aria-label="Woman in nude one-piece among palm fronds" style="background:radial-gradient(ellipse 60px 110px at 100px 170px,rgba(236,210,180,.9),transparent 70%),linear-gradient(120deg,#c8d3d6,#b8b874 50%,#d8c6a6)"><span class="shop-now display">Shop now</span></div><p class="name">Lorem ipsum dolor sit ame<br>nsecteturaelit seius.</p><p class="price">$299.00</p></div>
<div class="abs product" style="left:869px;top:2244px"><div class="photo photo-fill" role="img" aria-label="Woman in green belted one-piece among tropical leaves" style="background:radial-gradient(ellipse 55px 110px at 115px 180px,rgba(120,160,120,.8),transparent 70%),linear-gradient(180deg,#3d5e3a,#557a4a 50%,#2f4a2e)"></div><p class="name">Lorem ipsum dolor sit ame<br>nsecteturaelit seius.</p><p class="price">$299.00</p></div>

<div class="abs about-photo photo-fill" role="img" aria-label="Woman in white outfit and hat against green foliage"></div>
<h2 class="abs about-title display">About Quillmore</h2>
<p class="abs about-text">Lorem ipsum dolor sit amet, consectetur adipiscing elit, sed do eiusmod tempor incididunt ut labore et dolore magna aliqua. Quis ipsum suspendisse ultrices gravida. Risus commodo viverra maecenas accumsan lacus vel facilisis.</p>

<section class="abs banner photo-fill" style="left:0;width:589px;background:radial-gradient(ellipse 260px 70px at 300px 290px,rgba(190,130,90,.8),transparent 70%),linear-gradient(180deg,#232b20,#3d3a2e 50%,#4b4036)" role="img" aria-label="Woman in black bikini lounging poolside">
  <h2 class="display" style="left:81px">Lorem ipsum dolor sit<br>amet, consectetur</h2>
</section>
<section class="abs banner photo-fill" style="left:614px;width:586px;background:radial-gradient(ellipse 70px 160px at 150px 210px,rgba(220,190,160,.8),transparent 70%),linear-gradient(180deg,#2f3c2c,#67665a 50%,#1f2b22)" role="img" aria-label="Woman in nude one-piece standing by a pool among palms">
  <h2 class="display" style="left:255px">Lorem ipsum dolor sit<br>amet, consectetur</h2>
</section>

<footer class="abs site-footer">
  <div class="footer-brand display">Quillmore</div>
  <div class="footer-col" style="left:463px"><h3 class="display">Shop</h3><a>Men</a><a>Women</a><a>Kids</a></div>
  <div class="footer-col" style="left:663px"><h3 class="display">About</h3><a>About Us</a><a>My Account</a><a>Blogs</a></div>
  <div class="footer-col" style="left:887px"><h3 class="display">Customer service</h3><a>Contact</a><a>Shipping Policy</a><a>Return/Exchange Policy</a></div>
  <div class="footer-rule"></div>
  <a class="social" style="left:127px" aria-label="Follow us"><svg viewBox="0 0 16 16"><path d="M4 12L12 4M6 4h6v6"/></svg></a>
  <a class="social" style="left:173px" aria-label="Share"><svg viewBox="0 0 16 16"><path d="M4 12L12 4M6 4h6v6"/></svg></a>
  <span class="legal" style="left:288px">© 2025 Quillmore. All Rights are Reserved</span>
  <span class="legal" style="left:729px">Terms and Conditions</span>
  <span class="legal" style="left:966px">Privacy Policy</span>
</footer>

</body>
</html>
```